THE TALL COPPER ATLAS OF PORTS

subtitle: AN INTRO TO SEARCH ENGINE OPTIMIZATION
background: white
dimensions: 1562x2500

Target Market(s)

Marketing professionals

Industry/Entity Type

Digital Marketing

Font styles to use
Sans Serif

Colors
ffffff
1b1b1b
3176b5

Requirements
Should not have
• Images or graphics

```html
<!DOCTYPE html>
<html lang="en">
<head>
<meta charset="utf-8">
<title>The Tall Copper Atlas of Ports — An Intro to Search Engine Optimization</title>
<link rel="stylesheet" href="https://fonts.googleapis.com/css2?family=Bebas+Neue&family=Oswald:wght@600&display=swap">
<style>
  :root {
    --backdrop: #ababab;
    --paper: #ffffff;
    --sky-light: #a9cdef;
    --sky-deep: #79a6d3;
    --ink: #1b1b1b;
    --navy: #0e3283;
    --rule-blue: #3176b5;
  }
  html, body {
    margin: 0;
    padding: 0;
    width: 1200px;
    height: 1200px;
    overflow: hidden;
    background: var(--backdrop);
  }
  .canvas {
    position: relative;
    width: 1200px;
    height: 1200px;
    font-family: "Bebas Neue", "Arial Narrow", sans-serif;
  }
  .cover {
    position: absolute;
    left: 255px;
    top: 48px;
    width: 690px;
    height: 1104px;
    background: linear-gradient(112deg,
      var(--sky-light) 0%,
      var(--paper) 40%,
      var(--paper) 50%,
      var(--sky-deep) 100%);
    overflow: hidden;
  }
  .cover > * {
    position: absolute;
    margin: 0;
    line-height: 1;
    white-space: nowrap;
    font-weight: 400;
  }
  .book-title {
    left: 0;
    width: 690px;
    top: 68px;
    text-align: center;
    font-family: "Oswald", "Arial Narrow", sans-serif;
    font-weight: 600;
    font-size: 30px;
    letter-spacing: 5px;
    padding-left: 5px;
    box-sizing: border-box;
    color: var(--navy);
  }
  .title-lead {
    left: 63px;
    top: 244px;
    font-size: 64px;
    letter-spacing: 4px;
    color: var(--ink);
  }
  .acronym-row {
    display: flex;
    align-items: baseline;
    left: 57px;
  }
  .acronym-row .initial {
    display: inline-block;
    width: 73px;
    font-size: 167px;
    color: var(--ink);
  }
  .acronym-row .rest {
    font-size: 120px;
    color: var(--navy);
  }
  .row-search { top: 315px; }
  .row-search .rest { letter-spacing: 7px; }
  .row-engine { top: 463px; }
  .row-engine .initial { width: 88px; }
  .row-engine .rest { letter-spacing: 21px; }
  .row-optimization { top: 618px; left: 55px; }
  .row-optimization .initial { width: 75px; }
  .row-optimization .rest { letter-spacing: 5px; }
  .title-rule {
    left: 57px;
    top: 778px;
    width: 574px;
    height: 4px;
    background: var(--rule-blue);
  }
  .author {
    left: 0;
    width: 690px;
    top: 994px;
    text-align: center;
    font-family: "Oswald", "Arial Narrow", sans-serif;
    font-weight: 600;
    font-size: 42px;
    letter-spacing: 22px;
    padding-left: 22px;
    box-sizing: border-box;
    color: var(--navy);
  }
</style>
</head>
<body>
  <main class="canvas">
    <article class="cover">
      <p class="book-title">The Tall Copper Atlas of Ports</p>
      <h1 class="title-lead">An Intro To</h1>
      <div class="acronym-row row-search"><span class="initial">S</span><span class="rest">EARCH</span></div>
      <div class="acronym-row row-engine"><span class="initial">E</span><span class="rest">NGINE</span></div>
      <div class="acronym-row row-optimization"><span class="initial">O</span><span class="rest">PTIMIZATION</span></div>
      <div class="title-rule"></div>
      <p class="author">Author Name</p>
    </article>
  </main>
</body>
</html>
```